Electronic hardware design and manufacturer needing a new business card design.

We need a new business card design consisting of a double sided design adhering to brand and logo guidelines attached. I also want to incorporate something that recognizes our 25th year in business ("EST 2001" or something like that....).

Need extra days to review

Need extra days to review

```html
<!DOCTYPE html>
<html lang="en">
<head>
<meta charset="utf-8">
<title>Brightline Circuit Co. — Business Card</title>
<link href="https://fonts.googleapis.com/css2?family=Montserrat:wght@400;500;700;800&display=swap" rel="stylesheet">
<style>
  :root {
    --backdrop: #d8d8d8;
    --card-navy: #152536;
    --ink-blue: #a8c4e0;
    --accent-amber: #f6ad00;
  }
  * { box-sizing: border-box; margin: 0; padding: 0; }
  html, body {
    width: 1200px; height: 846px; overflow: hidden;
    background: var(--backdrop);
    font-family: "Montserrat", sans-serif;
  }
  .sheet {
    position: relative; width: 1200px; height: 846px;
    display: flex; align-items: center; justify-content: center; gap: 44px;
  }
  .card {
    position: relative; width: 540px; height: 309px;
    background: var(--card-navy); color: var(--ink-blue);
    border-radius: 3px;
    box-shadow: 0 10px 28px rgba(0,0,0,.18);
    overflow: hidden;
  }
  .brand {
    display: flex; align-items: center; gap: 10px;
    color: var(--ink-blue); font-weight: 800; letter-spacing: .02em;
  }
  .brand-mark { width: 14px; height: 14px; background: var(--accent-amber); flex: none; }
  .brand-name { line-height: 1.1; }

  /* front side */
  .card-front .brand { position: absolute; left: 38px; top: 118px; font-size: 17px; }
  .person { position: absolute; left: 262px; top: 88px; }
  .person-name { font-weight: 800; font-size: 25px; letter-spacing: .01em; }
  .person-title { font-weight: 500; font-size: 14px; letter-spacing: .08em; margin-top: 2px; }
  .contact {
    position: absolute; left: 38px; right: 24px; bottom: 34px;
    font-size: 11px; font-weight: 500; line-height: 1;
    display: flex; flex-direction: column; gap: 10px;
  }
  .contact-row { display: flex; align-items: center; gap: 7px; white-space: nowrap; }
  .contact-item { display: flex; align-items: center; gap: 5px; }
  .icon { width: 15px; height: 15px; flex: none; }

  /* back side */
  .card-back { display: flex; flex-direction: column; align-items: center; justify-content: center; }
  .card-back .brand { font-size: 24px; }
  .founding { margin-top: 12px; font-weight: 500; font-size: 14px; letter-spacing: .14em; }
</style>
</head>
<body>
<main class="sheet">

  <section class="card card-front" aria-label="Card front">
    <div class="brand">
      <span class="brand-mark"></span>
      <span class="brand-name">BRIGHTLINE<br>CIRCUIT CO.</span>
    </div>

    <div class="person">
      <p class="person-name">Alex Morgan</p>
      <p class="person-title">TITLE</p>
    </div>

    <div class="contact">
      <div class="contact-row">
        <span class="contact-item">
          <svg class="icon" viewBox="0 0 16 16" aria-hidden="true"><rect width="16" height="16" rx="1.5" fill="#a8c4e0"/><path d="M5 3.5l2 2-1 1.2c.6 1.4 1.7 2.5 3.1 3.1l1.2-1 2 2-1.2 1.7C7.6 12.3 3.9 8.6 3.4 4.8z" fill="#152536"/></svg>
          (555) 014-2290
        </span>
        <span class="contact-item">
          <svg class="icon" viewBox="0 0 16 16" aria-hidden="true"><rect width="16" height="16" rx="1.5" fill="#a8c4e0"/><path d="M5 3.5l2 2-1 1.2c.6 1.4 1.7 2.5 3.1 3.1l1.2-1 2 2-1.2 1.7C7.6 12.3 3.9 8.6 3.4 4.8z" fill="#152536"/></svg>
          Toll-free (800) 555-0142
        </span>
        <span class="contact-item">
          <svg class="icon" viewBox="0 0 16 16" aria-hidden="true"><rect width="16" height="16" rx="1.5" fill="#a8c4e0"/><g fill="none" stroke="#152536" stroke-width="1"><circle cx="8" cy="8" r="4.6"/><ellipse cx="8" cy="8" rx="2" ry="4.6"/><path d="M3.4 8h9.2M4.2 5.6h7.6M4.2 10.4h7.6"/></g></svg>
          brightlinecircuit.ca
        </span>
      </div>
      <div class="contact-row">
        <span class="contact-item">
          <svg class="icon" viewBox="0 0 16 16" aria-hidden="true"><rect width="16" height="16" rx="1.5" fill="#a8c4e0"/><path d="M8 2.8a3.6 3.6 0 0 0-3.6 3.6C4.4 9 8 13.2 8 13.2s3.6-4.2 3.6-6.8A3.6 3.6 0 0 0 8 2.8zm0 5a1.4 1.4 0 1 1 0-2.8 1.4 1.4 0 0 1 0 2.8z" fill="#152536"/></svg>
          410 Harbour Road, Unit 7, Riverton, Alberta T0X 1A0
        </span>
      </div>
    </div>
  </section>

  <section class="card card-back" aria-label="Card back">
    <div class="brand">
      <span class="brand-mark"></span>
      <span class="brand-name">BRIGHTLINE CIRCUIT CO.</span>
    </div>
    <p class="founding">EST 2001</p>
  </section>

</main>
</body>
</html>
```